Medical Company in need of Modern business card design for new Wound Care clinic.

Modern business card design for our Woundcare company. Logo and description of services can be found on our website; https://www.tovrel-woundcare.com/

```html
<!DOCTYPE html>
<html lang="en">
<head>
<meta charset="utf-8">
<title>Tovrel Woundcare – Business Card</title>
<link rel="stylesheet" href="https://fonts.googleapis.com/css2?family=Montserrat:wght@400;500;700&display=swap">
<style>
  :root {
    --bg: #e9e7e4;
    --paper: #ffffff;
    --ink: #1d1d1d;
    --night: #121212;
    --gold: #c8962a;
    --gold-soft: #e2b24c;
  }
  * { box-sizing: border-box; margin: 0; padding: 0; }
  html, body { width: 1200px; height: 786px; overflow: hidden; }
  body {
    background: var(--bg);
    font-family: "Montserrat", sans-serif;
    color: var(--ink);
    position: relative;
  }
  .card {
    position: absolute;
    top: 238px;
    width: 540px;
    height: 310px;
    box-shadow: 0 8px 24px rgba(0,0,0,.18);
  }
  .card--front { left: 40px; background: var(--paper); }
  .card--back { left: 620px; background: var(--night); display: flex; align-items: center; justify-content: center; }

  .brand-name {
    position: absolute;
    left: 30px;
    top: 70px;
    font-size: 21px;
    font-weight: 500;
    letter-spacing: 6px;
    color: var(--ink);
  }
  .card--back .brand-name {
    position: static;
    color: #ffffff;
    font-size: 26px;
    letter-spacing: 7px;
  }

  .services {
    position: absolute;
    right: 30px;
    top: 24px;
    text-align: right;
    list-style: none;
  }
  .services__title {
    color: var(--gold);
    font-weight: 700;
    font-size: 15px;
    margin-bottom: 4px;
  }
  .services li {
    font-size: 11px;
    line-height: 14px;
    color: var(--ink);
  }
  .services li::after {
    content: "";
    display: inline-block;
    width: 4px; height: 4px;
    border-radius: 50%;
    background: var(--gold-soft);
    margin-left: 5px;
    vertical-align: middle;
  }
  .services li.cont::after { visibility: hidden; }

  .divider {
    position: absolute;
    left: 30px; right: 30px;
    top: 158px;
    height: 1.5px;
    background: var(--gold-soft);
  }

  .person { position: absolute; left: 30px; top: 172px; }
  .person__name { color: var(--gold); font-weight: 700; font-size: 21px; }
  .person__role { font-size: 12px; font-weight: 500; margin-top: 1px; }
  .person__rule { width: 170px; height: 1.5px; background: var(--gold-soft); margin-top: 6px; }

  .contacts { position: absolute; left: 30px; top: 232px; list-style: none; }
  .contacts li {
    display: flex; align-items: center; gap: 10px;
    font-size: 12.5px; line-height: 22px;
  }
  .contacts svg { width: 12px; height: 12px; fill: none; stroke: var(--gold); stroke-width: 2; }

  .address {
    position: absolute;
    right: 30px;
    top: 178px;
    text-align: right;
    font-size: 12px;
    line-height: 15px;
  }
</style>
</head>
<body>
  <section class="card card--front" aria-label="Business card front">
    <div class="brand-name">TOVREL WOUNDCARE</div>

    <ul class="services">
      <li class="services__title" style="list-style:none">Our Services</li>
      <li>Hyperbaric Oxygen Therapy</li>
      <li class="cont">(HBO): A Cornerstone of</li>
      <li class="cont">Advanced Wound Care</li>
      <li>Debridement</li>
      <li>Advanced Wound Dressings</li>
      <li>Bio-engineered Skin Substitutes</li>
      <li>Compression Therapy and</li>
      <li>Edema Management</li>
    </ul>

    <div class="divider"></div>

    <div class="person">
      <div class="person__name">Daniel Harlow</div>
      <div class="person__role">Managing Director</div>
      <div class="person__rule"></div>
    </div>

    <ul class="contacts">
      <li>
        <svg viewBox="0 0 24 24" aria-hidden="true"><path d="M5 3h4l2 5-3 2a12 12 0 0 0 6 6l2-3 5 2v4a2 2 0 0 1-2 2A17 17 0 0 1 3 5a2 2 0 0 1 2-2z"/></svg>
        555.010.2247
      </li>
      <li>
        <svg viewBox="0 0 24 24" aria-hidden="true"><rect x="3" y="5" width="18" height="14" rx="1"/><path d="M3 6l9 7 9-7"/></svg>
        info@tovrel-woundcare.com
      </li>
      <li>
        <svg viewBox="0 0 24 24" aria-hidden="true"><circle cx="12" cy="12" r="9"/><path d="M3 12h18M12 3c3 3 3 15 0 18M12 3c-3 3-3 15 0 18"/></svg>
        www.tovrel-woundcare.com
      </li>
    </ul>

    <div class="address">48 Cedar Hollow Lane<br>Ridgeton, MS 39000</div>
  </section>

  <section class="card card--back" aria-label="Business card back">
    <div class="brand-name">TOVREL WOUNDCARE</div>
  </section>
</body>
</html>
```